White Paper and One-Page Advertisement for TELVAMORE-QX

I need both documents to be better formatted and designed so they look professional, not something someone with mediocre word skills put together. They will go out to 1000s of industry professionals, and they need to look sharp. I need them to have my company's color palate logo, and branding on it similar to how it is now, but better. Please do not change any of the written content, but it can be arranged in any other format you think is better. Smart art and things i've already used can be omitted in favor of better designs. The developer is free to use their creativity. White paper should not be longer than the three pages unless necessary.

Target Market(s)

Life Sciences supply chain professionals

Colors
33b8a4
0592cd
9bcb3c
fbee3e
3277b5

Requirements
Must have
• Must be professional looking and not look like something done in word. Please use the color palate as seen on the documents.
Should not have
• Any changes to the written content.

```html
<!DOCTYPE html>
<html lang="en">
<head>
<meta charset="utf-8">
<title>TELVAMORE-QX — One-Page Advertisement</title>
<link href="https://fonts.googleapis.com/css2?family=Russo+One&family=Open+Sans:wght@400;600;700&family=Exo+2:wght@400&display=swap" rel="stylesheet">
<style>
  :root {
    --teal-dark: #0e7a64;
    --teal: #1a8a6e;
    --green: #56a84a;
    --lime: #7cba44;
    --lime-bright: #9bcb3c;
    --ink: #555a5e;
    --ink-dark: #4a4f52;
    --white: #ffffff;
    --page-bg: #ffffff;
  }
  * { box-sizing: border-box; margin: 0; padding: 0; }
  html, body { width: 1200px; height: 1200px; overflow: hidden; background: var(--page-bg); }
  .flyer {
    position: absolute; left: 214px; top: 54px; width: 772px; height: 1090px;
    background: var(--white);
    box-shadow: 3px 3px 4px rgba(0,0,0,0.35);
    overflow: hidden;
    font-family: "Open Sans", sans-serif;
  }
  .flyer-shapes { position: absolute; inset: 0; }
  .brand {
    position: absolute; left: 38px; top: 380px; width: 264px; height: 180px;
    display: flex; align-items: center; justify-content: center; gap: 8px;
  }
  .brand-dot { width: 16px; height: 16px; border-radius: 50%; background: var(--lime); flex: none; }
  .brand-name {
    font-family: "Open Sans", sans-serif; font-weight: 700; font-size: 25px;
    color: var(--teal-dark); letter-spacing: 0.5px;
  }
  .section-title {
    font-family: "Russo One", sans-serif; font-size: 29px; line-height: 1; letter-spacing: 0.5px;
  }
  .checklist { list-style: none; font-size: 14.6px; line-height: 17px; }
  .checklist li { position: relative; padding-left: 20px; margin-bottom: 11px; }
  .checklist li::before {
    content: "\2713"; position: absolute; left: 0; top: 1px; font-size: 14px;
  }
  .panel-left { position: absolute; left: 27px; width: 345px; color: var(--white); }
  .platform { top: 612px; }
  .promise { top: 953px; }
  .panel-left .section-title { color: var(--white); margin-bottom: 17px; }
  .panel-right { position: absolute; left: 415px; width: 340px; color: var(--ink); }
  .benefits { top: 612px; }
  .benefits .section-title { color: var(--teal-dark); margin-bottom: 17px; }
  .benefits .checklist li { margin-bottom: 12px; }
  .contact { top: 953px; }
  .contact-title {
    font-family: "Exo 2", sans-serif; font-size: 33px; color: var(--teal-dark); line-height: 1; margin-bottom: 12px;
  }
  .contact-line { display: flex; align-items: center; gap: 12px; font-size: 16.5px; color: var(--ink); margin-bottom: 5px; }
  .contact-line b { font-weight: 700; color: var(--ink-dark); }
  .contact-line svg { flex: none; }
  .white-paper {
    position: absolute; right: 18px; top: 1056px; font-weight: 700; font-size: 15.5px; color: var(--ink-dark);
  }
  .white-paper span { color: var(--lime-bright); }
</style>
</head>
<body>
<div class="flyer">
  <svg class="flyer-shapes" width="772" height="1090" viewBox="0 0 772 1090">
    <defs>
      <linearGradient id="panelGradient" x1="0" y1="0" x2="0.3" y2="1">
        <stop offset="0" stop-color="#7cba44"/>
        <stop offset="0.35" stop-color="#56a84a"/>
        <stop offset="1" stop-color="#1a8a6e"/>
      </linearGradient>
      <linearGradient id="photoGradient" x1="0" y1="0" x2="1" y2="1">
        <stop offset="0" stop-color="#4a2e22"/>
        <stop offset="0.45" stop-color="#8a6a4c"/>
        <stop offset="1" stop-color="#2f5a5e"/>
      </linearGradient>
    </defs>
    <path d="M0,240 C40,380 140,460 300,512 L387,512 L387,1090 L0,1090 Z" fill="url(#panelGradient)"/>
    <path d="M0,0 H772 V410 C772,500 700,552 620,552 C570,552 535,532 495,500 L300,504 C150,470 30,380 0,230 Z"
          fill="url(#photoGradient)" role="img" aria-label="Photo: two women smiling as they tie a ceremonial thread around the wrist of a young person in traditional dress"/>
    <ellipse cx="170" cy="585" rx="92" ry="8" fill="#3d6d3a" opacity="0.5"/>
    <ellipse cx="170" cy="470" rx="134" ry="114" fill="#ffffff"/>
    <path d="M60,405 A134,114 0 0 1 302,455" fill="none" stroke="#0e7a64" stroke-width="4"/>
    <path d="M302,480 A134,114 0 0 1 150,583" fill="none" stroke="#0e7a64" stroke-width="2"/>
  </svg>

  <div class="brand">
    <span class="brand-dot"></span>
    <span class="brand-name">TELVAMORE-QX</span>
  </div>

  <section class="panel-left platform">
    <h2 class="section-title">OUR PLATFORM</h2>
    <ul class="checklist">
      <li>A multi-vendor marketplace for the life science community to transact pre-market and after-market materials and equipment</li>
      <li>Researchers, manufactures, and original suppliers can create an account to buy, sell, or donate materials</li>
      <li>Part 11 compliant signature and authentication</li>
      <li>Leverages industry auditing skills to facilitate compliant and transparent transactions</li>
      <li>Some of the best and industry vendors and software used</li>
    </ul>
  </section>

  <section class="panel-left promise">
    <h2 class="section-title">OUR PROMISE</h2>
    <ul class="checklist">
      <li>A greener, more cost-efficient, and quality driven supply chain through a collaborative life sciences marketplace.</li>
    </ul>
  </section>

  <section class="panel-right benefits">
    <h2 class="section-title">BENEFITS</h2>
    <ul class="checklist">
      <li>Reduce write-offs by selling excess and obsolete materials, equipment, spare parts, etc.</li>
      <li>Buy quality materials at a reduced price.</li>
      <li>Market materials if an original supplier</li>
      <li>Donate material to researchers</li>
      <li>Acquire donated materials</li>
      <li>Collaborate and consort to reduce supply chain risk such as mutual aid agreements, joint supplier audits, etc.</li>
    </ul>
  </section>

  <section class="panel-right contact">
    <h2 class="contact-title">CONTACT US</h2>
    <p class="contact-line">
      <svg width="13" height="13" viewBox="0 0 14 14"><g fill="none" stroke="#7cba44" stroke-width="1.3"><circle cx="7" cy="7" r="6"/><ellipse cx="7" cy="7" rx="2.6" ry="6"/><path d="M1,7 H13 M2,4 H12 M2,10 H12"/></g></svg>
      <span>www.<b>telvamoreqx</b>.com</span>
    </p>
    <p class="contact-line">
      <svg width="13" height="13" viewBox="0 0 14 14"><rect x="1" y="3" width="12" height="8" fill="#7cba44"/><path d="M1,3 L7,8 L13,3" fill="none" stroke="#ffffff" stroke-width="1.2"/></svg>
      <span>info@<b>telvamoreqx</b>.com</span>
    </p>
  </section>

  <p class="white-paper">READ OUR <span>WHITE PAPER</span></p>
</div>
</body>
</html>
```